Label

I need a label designed for a bottle of water. I like the lightning bolt and the blue. But I do not want it exactly like the Zimm-ooh.

The label needs to be 9 inches by 2.5 inches.

Logo Text

Mesa Spring: Sip the Mesa

```html
<!DOCTYPE html>
<html lang="en">
<head>
<meta charset="utf-8">
<title>Mesa Spring – Bottle Label</title>
<link rel="stylesheet" href="https://fonts.googleapis.com/css2?family=Lato:wght@400;700;900&display=swap">
<style>
  :root {
    --page-bg: #eef2f6;
    --sky-top: #6f9fd3;
    --sky-mid: #b9d2ec;
    --sky-haze: #e3edf7;
    --band-deep: #2f6fb8;
    --band-light: #5f97d2;
    --ink-navy: #1d3f78;
    --ink-white: #ffffff;
  }
  * { margin: 0; padding: 0; box-sizing: border-box; }
  html, body {
    width: 1200px;
    height: 1146px;
    overflow: hidden;
    background: var(--page-bg);
  }
  .canvas {
    position: relative;
    width: 1200px;
    height: 1146px;
    display: flex;
    align-items: center;
    justify-content: center;
  }
  .label {
    position: relative;
    width: 1080px;
    height: 300px;
    overflow: hidden;
    box-shadow: 0 10px 30px rgba(29, 63, 120, 0.18);
  }
  .label__sky {
    position: absolute;
    inset: 0;
    background:
      radial-gradient(ellipse 40% 60% at 50% 40%, rgba(255,255,255,0.75), rgba(255,255,255,0) 70%),
      linear-gradient(180deg, var(--sky-top) 0%, var(--sky-mid) 45%, var(--sky-haze) 62%, var(--band-light) 80%, var(--band-deep) 100%);
  }
  .label__front {
    position: absolute;
    left: 50%;
    top: 0;
    width: 520px;
    height: 100%;
    transform: translateX(-50%);
    display: flex;
    flex-direction: column;
    align-items: center;
    font-family: "Lato", sans-serif;
  }
  .brand {
    margin-top: 46px;
    font-weight: 900;
    font-size: 60px;
    letter-spacing: 1px;
    color: var(--ink-navy);
    line-height: 1;
    white-space: nowrap;
  }
  .tagline {
    margin-top: 14px;
    font-weight: 700;
    font-size: 17px;
    letter-spacing: 1.5px;
    text-transform: uppercase;
    color: var(--ink-navy);
  }
  .product {
    margin-top: 34px;
    text-align: center;
    color: var(--ink-white);
  }
  .product__kind {
    font-weight: 400;
    font-size: 15px;
    letter-spacing: 9px;
    text-transform: uppercase;
  }
  .product__name {
    margin-top: 4px;
    font-weight: 700;
    font-size: 22px;
    letter-spacing: 1.5px;
    text-transform: uppercase;
  }
</style>
</head>
<body>
  <main class="canvas">
    <section class="label" aria-label="Mesa Spring water bottle label">
      <div class="label__sky" role="img" aria-label="Soft blue sky with white clouds fading into a deep blue band"></div>

      <div class="label__front">
        <h1 class="brand">Mesa Spring</h1>
        <p class="tagline">Sip the Mesa</p>

        <div class="product">
          <p class="product__kind">Natural</p>
          <p class="product__name">Spring Water</p>
        </div>
      </div>
    </section>
  </main>
</body>
</html>
```